Progressive/contemporary business card design for successful Startups as a Service Company

New logo launched in 2020. New website launched in 2021. Now that COVID is (mostly) behind us, I'm networking with more people and need a business card that matches the company/logo design aesthetic.

```html
<!DOCTYPE html>
<html lang="en">
<head>
<meta charset="utf-8">
<title>Northquill Business Card</title>
<link rel="stylesheet" href="https://fonts.googleapis.com/css2?family=Montserrat:wght@300;400;500&display=swap">
<style>
  :root {
    --bg-top: #d6d7d5;
    --bg-bottom: #8a8a8a;
    --card: #060606;
    --brand-text: #e4e4e4;
    --name-text: #8d8d8d;
    --detail-text: #9a9a9a;
    --icon: #6a6a6a;
    --line-blue: #2aa3dc;
    --line-violet: #b23bbd;
    --line-green: #6cc04a;
    --line-orange: #f08a24;
  }
  * { box-sizing: border-box; margin: 0; padding: 0; }
  html, body { width: 1200px; height: 903px; overflow: hidden; }
  body {
    background: linear-gradient(180deg, var(--bg-top) 0%, var(--bg-bottom) 100%);
    font-family: "Montserrat", sans-serif;
    position: relative;
  }
  .card {
    position: absolute;
    left: 350px;
    width: 500px;
    height: 286px;
    background: var(--card);
    box-shadow: 0 10px 30px rgba(0,0,0,0.25);
  }
  .card--front { top: 140px; display: flex; align-items: center; justify-content: center; }
  .card--back { top: 476px; }
  .brand {
    display: flex;
    align-items: center;
    gap: 12px;
  }
  .brand__name {
    color: var(--brand-text);
    font-weight: 400;
    font-size: 28px;
    letter-spacing: 5px;
  }
  .brand__mark {
    width: 14px;
    height: 14px;
    background: var(--brand-text);
  }
  .contact {
    position: absolute;
    right: 30px;
    bottom: 26px;
    text-align: right;
  }
  .contact__name {
    color: var(--name-text);
    font-weight: 300;
    font-size: 13px;
    letter-spacing: 0.5px;
    text-transform: uppercase;
  }
  .contact__role {
    color: var(--detail-text);
    font-weight: 400;
    font-size: 11px;
    margin-top: 2px;
  }
  .contact__rule {
    display: inline-block;
    width: 44px;
    height: 1.5px;
    margin: 8px 0 8px;
    background: linear-gradient(90deg, var(--line-orange), var(--line-green), var(--line-blue), var(--line-violet));
  }
  .contact__list { list-style: none; }
  .contact__item {
    display: flex;
    justify-content: flex-end;
    align-items: center;
    gap: 6px;
    color: var(--detail-text);
    font-size: 10px;
    font-weight: 400;
    line-height: 15px;
  }
  .contact__icon { width: 8px; height: 8px; }
</style>
</head>
<body>
  <section class="card card--front">
    <div class="brand">
      <span class="brand__name">NORTHQUILL</span>
      <span class="brand__mark"></span>
    </div>
  </section>

  <section class="card card--back">
    <div class="contact">
      <p class="contact__name">Avery Lane Morgan</p>
      <p class="contact__role">President</p>
      <span class="contact__rule"></span>
      <ul class="contact__list">
        <li class="contact__item">(555) 018-2047
          <svg class="contact__icon" viewBox="0 0 10 10" aria-hidden="true"><path d="M2 1 L4 1 L4.6 3.2 L3.4 4 Q4.4 6 6 6.6 L6.8 5.4 L9 6 L9 8 Q5 9 2 6 Q0.8 4 2 1 Z" fill="var(--icon)"/></svg>
        </li>
        <li class="contact__item">hello@northquillgroup.com
          <svg class="contact__icon" viewBox="0 0 10 10" aria-hidden="true"><rect x="0.5" y="2" width="9" height="6" fill="none" stroke="var(--icon)"/><path d="M0.5 2 L5 5.5 L9.5 2" fill="none" stroke="var(--icon)"/></svg>
        </li>
        <li class="contact__item">www.northquillgroup.com
          <svg class="contact__icon" viewBox="0 0 10 10" aria-hidden="true"><circle cx="5" cy="5" r="4.3" fill="none" stroke="var(--icon)"/><path d="M0.7 5 H9.3 M5 0.7 Q2.5 5 5 9.3 M5 0.7 Q7.5 5 5 9.3" fill="none" stroke="var(--icon)" stroke-width="0.7"/></svg>
        </li>
      </ul>
    </div>
  </section>
</body>
</html>
```